Business card for medical clinic

I need an upmarket, modern medical/health business card for my clinic

Contact Information for Business Card

name, address, email, qr code

```html
<!DOCTYPE html>
<html lang="en">
<head>
<meta charset="utf-8">
<title>Meridian Care Clinic – Business Card</title>
<link rel="stylesheet" href="https://fonts.googleapis.com/css2?family=Crimson+Text:wght@400;600&display=swap">
<style>
  :root {
    --backdrop: #e4e5e7;
    --paper: #ffffff;
    --navy: #14203f;
    --sky: #22a9e2;
    --brand: #1d5d92;
    --ink: #3a3a3a;
    --card-w: 520px;
    --card-h: 297px;
  }
  * { box-sizing: border-box; margin: 0; padding: 0; }
  html, body {
    width: 1200px; height: 800px; overflow: hidden;
    background: var(--backdrop);
    font-family: "Crimson Text", Georgia, serif;
  }
  .canvas {
    width: 1200px; height: 800px;
    display: flex; align-items: center; justify-content: center; gap: 60px;
  }
  .card {
    position: relative;
    width: var(--card-w); height: var(--card-h);
    background: var(--paper);
    overflow: hidden;
    box-shadow: 0 6px 18px rgba(0,0,0,0.12);
  }

  /* brand lockup */
  .brand {
    position: absolute;
    display: flex; align-items: center; gap: 10px;
    color: var(--brand);
  }
  .brand-mark {
    width: 40px; height: 40px; border-radius: 50%;
    border: 3px solid var(--brand);
    flex: none;
  }
  .brand-name {
    font-weight: 600; letter-spacing: 0.12em; text-transform: uppercase;
    line-height: 1.1;
  }

  /* bottom bands */
  .band-navy, .tab-sky { position: absolute; bottom: 0; }
  .band-navy { height: 34px; background: var(--navy); }
  .tab-sky {
    height: 62px; background: var(--sky);
    display: flex; align-items: center; justify-content: center;
    color: var(--navy); font-size: 17px;
  }

  /* back side */
  .card-back .brand { left: 50%; top: 96px; transform: translateX(-42%); }
  .card-back .brand-mark { width: 64px; height: 64px; }
  .card-back .brand-name { font-size: 26px; }
  .card-back .tab-sky { left: 0; width: 205px; border-top-right-radius: 16px; }
  .card-back .band-navy { left: 190px; right: 0; }

  /* front side */
  .contact { position: absolute; left: 34px; top: 30px; color: var(--ink); }
  .person-name { color: var(--sky); font-size: 20px; font-weight: 600; letter-spacing: 0.03em; text-transform: uppercase; line-height: 1; }
  .person-role { font-size: 16px; margin-bottom: 16px; }
  .address { font-size: 16px; line-height: 1.2; margin-bottom: 10px; }
  .contact-line { display: flex; align-items: center; gap: 6px; font-size: 16px; line-height: 1.3; }
  .contact-line svg { width: 12px; height: 12px; fill: var(--navy); flex: none; }
  .card-front .brand { right: 30px; top: 112px; }
  .card-front .brand-mark { width: 48px; height: 48px; }
  .card-front .brand-name { font-size: 20px; }
  .card-front .band-navy { left: 0; width: 330px; }
  .card-front .tab-sky { left: 318px; right: 0; border-top-left-radius: 16px; }
</style>
</head>
<body>
<main class="canvas">

  <section class="card card-back" aria-label="Card back">
    <div class="brand">
      <span class="brand-mark"></span>
      <span class="brand-name">Meridian Care<br>Clinic</span>
    </div>
    <div class="tab-sky">meridiancareclinic.com</div>
    <div class="band-navy"></div>
  </section>

  <section class="card card-front" aria-label="Card front">
    <div class="contact">
      <p class="person-name">Daniel Hart</p>
      <p class="person-role">Director</p>
      <p class="address">00 dummy city<br>dummy place 0000</p>
      <p class="contact-line">
        <svg viewBox="0 0 24 24" aria-hidden="true"><path d="M6.6 10.8a15.1 15.1 0 0 0 6.6 6.6l2.2-2.2a1 1 0 0 1 1-.25 11.4 11.4 0 0 0 3.6.57 1 1 0 0 1 1 1V20a1 1 0 0 1-1 1A17 17 0 0 1 3 4a1 1 0 0 1 1-1h3.5a1 1 0 0 1 1 1c0 1.25.2 2.45.57 3.57a1 1 0 0 1-.25 1z"/></svg>
        300-555-0142
      </p>
      <p class="contact-line">
        <svg viewBox="0 0 24 24" aria-hidden="true"><path d="M2 5h20v14H2z M4 7v.4l8 5.2 8-5.2V7z" fill-rule="evenodd"/></svg>
        info@meridiancareclinic.com
      </p>
    </div>
    <div class="brand">
      <span class="brand-mark"></span>
      <span class="brand-name">Meridian Care<br>Clinic</span>
    </div>
    <div class="band-navy"></div>
    <div class="tab-sky">meridiancareclinic.com</div>
  </section>

</main>
</body>
</html>
```